Video Editing Website - Wordpress Design Project

Hi There
I am setting up a Tribute Funeral Video and Home Video Editing Website for my Company. "Reel Keepsake". This is to assist people with putting together their Videos and Photos with music to show at a Funeral or for Family Memories. I already have a domain www.reelkeepsake.com.au, but I have no host yet.

Some websites that already do this are http://www.lanternclips.com.au/tributes, http://www.hearthfilmcraft.com.au/services/funeral-tribute-videos.html, and http://www.quillmontage.com.au/
These are examples not to cpy, but to get an idea of what I am offering so you can design accordingly.

I have a logo which is attached. You will see that the logo is mainly blue, so I would appreciate a website with that colour on the pages, but not ALL over the page.

I would like to upload videos occasionally from flickstow.com so I would appreciate that option incorporated.

Thank you lots.
Callum

Target Market(s)

Families predominately in the 25-60 age range

Industry/Entity Type

It Company

Requirements
Must have
• *Ability to upload Videos from flickstow.com
*Ability for me to edit the content whenever I need to
*A contact page to send email messages to me

```html
<!DOCTYPE html>
<html lang="en">
<head>
<meta charset="utf-8">
<title>Reel Keepsake</title>
<link href="https://fonts.googleapis.com/css2?family=Ubuntu:wght@400;500;700&display=swap" rel="stylesheet">
<style>
  :root {
    --page-bg: #c8d6e4;
    --brand-blue: #2565b5;
    --slider-frame: #a3b9cf;
    --arrow-grey: #6b747c;
    --text-dark: #1a1a1a;
    --divider-dark: #2b2b2b;
    --white: #ffffff;
    --player-dark: #1f2427;
    --player-accent: #1aa9e6;
  }
  * { box-sizing: border-box; margin: 0; padding: 0; }
  html, body { width: 691px; height: 1200px; overflow: hidden; }
  body {
    position: relative;
    background: var(--page-bg);
    font-family: "Ubuntu", "Trebuchet MS", sans-serif;
    color: var(--text-dark);
  }

  /* Header */
  .brand {
    position: absolute; left: 66px; top: 60px;
    display: flex; align-items: center; gap: 8px;
    font-size: 24px; font-weight: 500; color: var(--brand-blue);
  }
  .brand-mark { width: 22px; height: 22px; border-radius: 50%; background: var(--brand-blue); }
  .main-nav {
    position: absolute; top: 76px; left: 370px;
    display: flex; gap: 27px;
    font-size: 14px; letter-spacing: 0.2px;
  }
  .main-nav a { color: var(--text-dark); text-decoration: none; }
  .main-nav a.is-current { color: var(--brand-blue); }

  /* Slider */
  .hero-slider {
    position: absolute; left: 33px; top: 102px; width: 625px; height: 202px;
    background: var(--slider-frame);
  }
  .hero-photo {
    position: absolute; left: 33px; top: 0; width: 559px; height: 202px;
    background: linear-gradient(180deg, #3e6f9c 0%, #6c99bd 55%, #a7c3d4 100%);
  }
  .slider-arrow { position: absolute; top: 86px; }
  .slider-arrow.prev { left: 9px; }
  .slider-arrow.next { left: 604px; }
  .slider-dots { position: absolute; left: 277px; top: 183px; display: flex; gap: 10px; }
  .slider-dots span { width: 10px; height: 10px; background: rgba(255,255,255,0.75); }

  /* Content */
  .section-title {
    position: absolute; left: 66px; width: 559px; height: 26px;
    background: var(--brand-blue); color: var(--white);
    font-size: 17px; font-weight: 700; text-align: center; line-height: 27px;
  }
  .body-copy {
    position: absolute; left: 66px; width: 559px;
    font-size: 11.6px; line-height: 13.8px; text-align: justify;
  }

  /* Video player */
  .video-player {
    position: absolute; left: 73px; top: 601px; width: 544px; height: 306px;
    background: linear-gradient(160deg, #8c8a84 0%, #6f7a6a 35%, #8da2b3 60%, #b3aea3 100%);
  }
  .player-tools { position: absolute; right: 8px; top: 9px; display: flex; flex-direction: column; gap: 6px; }
  .player-tools span {
    width: 37px; height: 28px; border-radius: 4px; background: rgba(31,36,39,0.85);
    color: var(--white); font-size: 7px; font-weight: 700; display: flex; align-items: flex-end; justify-content: center; padding-bottom: 3px;
  }
  .play-button {
    position: absolute; left: 9px; top: 264px; width: 55px; height: 34px;
    background: rgba(31,36,39,0.9); border-radius: 4px;
    display: flex; align-items: center; justify-content: center;
  }
  .player-bar {
    position: absolute; left: 73px; top: 272px; width: 463px; height: 26px;
    background: rgba(31,36,39,0.9); border-radius: 4px;
  }
  .progress-track {
    position: absolute; left: 9px; top: 9px; width: 390px; height: 8px;
    background: #555d62; border: 1px solid #8b9397;
  }
  .progress-fill { width: 80%; height: 100%; background: var(--player-accent); }
  .time-badge {
    position: absolute; left: 377px; top: 265px; width: 34px; height: 13px;
    background: var(--white); color: var(--text-dark); font-size: 9px; text-align: center; line-height: 13px; border-radius: 2px;
  }
  .volume-bars { position: absolute; left: 408px; top: 8px; }
  .fullscreen-icon { position: absolute; left: 444px; top: 8px; }

  /* Contact */
  .contact-divider { position: absolute; left: 0; top: 954px; width: 691px; height: 7px; background: var(--divider-dark); }
  .contact-area { position: absolute; left: 0; top: 961px; width: 691px; height: 239px; background: var(--brand-blue); }
  .contact-title {
    position: absolute; left: 32px; top: 13px; width: 626px; height: 26px;
    background: var(--white); color: var(--brand-blue);
    font-size: 18px; font-weight: 500; text-align: center; line-height: 27px;
  }
  .field-label {
    position: absolute; left: 110px; width: 100px; text-align: right;
    color: var(--white); font-size: 11.5px; font-weight: 500;
  }
  .field-input {
    position: absolute; left: 222px; width: 217px;
    border: 1px solid var(--white); background: transparent;
  }
  .submit-button {
    position: absolute; left: 385px; top: 196px; width: 54px; height: 17px;
    background: var(--white); color: var(--brand-blue); border: none;
    font-family: inherit; font-size: 11px; line-height: 17px; text-align: center;
  }
</style>
</head>
<body>
  <header>
    <div class="brand"><span class="brand-mark"></span>Reel Keepsake</div>
    <nav class="main-nav">
      <a class="is-current" href="#">HOME</a>
      <a href="#">ABOUT</a>
      <a href="#">SERVICE</a>
      <a href="#">CONTACT</a>
    </nav>
  </header>

  <section class="hero-slider">
    <div class="hero-photo" role="img" aria-label="Slide photo: dandelion silhouette against a blue evening sky"></div>
    <svg class="slider-arrow prev" width="12" height="30" viewBox="0 0 12 30"><polygon points="12,0 0,15 12,30" fill="var(--arrow-grey)"/></svg>
    <svg class="slider-arrow next" width="12" height="30" viewBox="0 0 12 30"><polygon points="0,0 12,15 0,30" fill="var(--arrow-grey)"/></svg>
    <div class="slider-dots"><span></span><span></span><span></span><span></span></div>
  </section>

  <h2 class="section-title" style="top:318px;">TOPIC TITLE GOES HERE</h2>
  <p class="body-copy" style="top:352px;">Aliquam vitae vehicula dui. Donec mi mi, condimentum et congue et, aliquet in ligula. Vivamus vitae dui odio. In consequat eu nibh non pulvinar. Fusce non mauris ipsum. Aenean adipiscing tincidunt quam, a venenatis neque euismod at. Quisque rhoncus vitae leo sit amet porta. Morbi vitae rhoncus dui. Ut mauris turpis, viverra non leo a, gravida commodo sapien. Ut tempus nulla eget lacus mollis adipiscing. Nunc tristique mauris a lacinia euismod.</p>
  <p class="body-copy" style="top:436px;">Fusce facilisis auctor arcu id dapibus. Nulla lobortis justo eget mi euismod, quis blandit justo placerat. Pellentesque auctor lacus a massa tempus volutpat. Vestibulum vel rutrum leo. Proin vel justo rutrum, porta orci sed, viverra sem. Etiam porta dictum iaculis. Cras nec vestibulum sem. Ut hendrerit, justo non hendrerit molestie, enim diam semper tortor, et convallis odio velit eu arcu. Aenean blandit tempus est, vitae rutrum sem sollicitudin consectetur.</p>

  <h2 class="section-title" style="top:514px;">TOPIC TITLE GOES HERE</h2>
  <p class="body-copy" style="top:548px;">Aliquam vitae vehicula dui. Donec mi mi, condimentum et congue et, aliquet in ligula. Vivamus vitae dui odio. In consequat eu nibh non pulvinar. Fusce non mauris ipsum. Aenean adipiscing tincidunt quam, a venenatis neque euismod at.</p>

  <div class="video-player" role="img" aria-label="Embedded video: weathered wooden posts on a pebble riverbank">
    <div class="player-tools"><span>SHARE</span><span>EMBED</span><span>HD</span></div>
    <div class="play-button">
      <svg width="16" height="18" viewBox="0 0 16 18"><polygon points="0,0 16,9 0,18" fill="var(--white)"/></svg>
    </div>
    <div class="time-badge">02:39</div>
    <div class="player-bar">
      <div class="progress-track"><div class="progress-fill"></div></div>
      <svg class="volume-bars" width="30" height="10" viewBox="0 0 30 10">
        <g fill="var(--player-accent)"><rect x="0" width="2" height="10"/><rect x="4" width="2" height="10"/><rect x="8" width="2" height="10"/><rect x="12" width="2" height="10"/><rect x="16" width="2" height="10"/><rect x="20" width="2" height="10"/><rect x="24" width="2" height="10"/></g>
      </svg>
      <svg class="fullscreen-icon" width="10" height="10" viewBox="0 0 10 10" fill="none" stroke="var(--white)" stroke-width="1.6">
        <path d="M1 1 L9 9 M9 1 L1 9"/>
      </svg>
    </div>
  </div>

  <p class="body-copy" style="top:917px;">Vestibulum vel rutrum leo. Proin vel justo rutrum, porta orci sed, viverra sem. Etiam porta dictum iaculis. Cras nec vestibulum sem. Ut hendrerit, justo non hendrerit molestie.</p>

  <div class="contact-divider"></div>
  <section class="contact-area">
    <h2 class="contact-title">CONTACT</h2>
    <label class="field-label" style="top:56px;">Name</label>
    <div class="field-input" style="top:52px;height:18px;"></div>
    <label class="field-label" style="top:87px;">E-mail</label>
    <div class="field-input" style="top:83px;height:18px;"></div>
    <label class="field-label" style="top:117px;">Content</label>
    <div class="field-input" style="top:114px;height:69px;"></div>
    <button class="submit-button" type="button">SUBMIT</button>
  </section>
</body>
</html>
```